BRV Stationary
BRV All The Way!
Corporate
Dale Orwick
CEO
2380 Tallow St. Suite #240 San Francisco, CA 94107
dorwick@brvatw.com
brvatw.com
looking for a water mark on the business cards and stationary. Check out the brief for the logo for more ideas. http://orders.markcraftdepot.com/contests/bright-relay-ventures/readbrief

```html
<!DOCTYPE html>
<html lang="en">
<head>
<meta charset="utf-8">
<title>BRV Business Card</title>
<link href="https://fonts.googleapis.com/css2?family=Open+Sans:wght@400;600;700;800&display=swap" rel="stylesheet">
<style>
  :root {
    --backdrop: #e7e4e0;
    --card: #ffffff;
    --brand-blue: #2d4f9c;
    --brand-green: #6aa13a;
    --ink: #2a2a2a;
    --divider: #7f8f5a;
  }
  * { margin: 0; padding: 0; box-sizing: border-box; }
  html, body {
    width: 1200px;
    height: 965px;
    overflow: hidden;
    background: var(--backdrop);
    font-family: "Open Sans", Arial, sans-serif;
  }
  .business-card {
    position: absolute;
    left: 243px;
    top: 235px;
    width: 774px;
    height: 439px;
    background: var(--card);
    border-radius: 30px;
    box-shadow: 0 6px 18px rgba(0, 0, 0, 0.18);
  }
  .brand {
    position: absolute;
    left: 31px;
    top: 140px;
    width: 340px;
    text-align: center;
  }
  .brand-name {
    display: block;
    font-size: 150px;
    font-weight: 800;
    line-height: 160px;
    letter-spacing: -4px;
    color: var(--brand-blue);
  }
  .brand-tagline {
    display: block;
    margin-top: 10px;
    font-size: 16px;
    font-weight: 700;
    letter-spacing: 0.6px;
    text-transform: uppercase;
    color: var(--brand-blue);
  }
  .divider {
    position: absolute;
    left: 408px;
    top: 105px;
    width: 2px;
    height: 255px;
    background: linear-gradient(to bottom, rgba(127,143,90,0), var(--divider) 20%, var(--divider) 80%, rgba(127,143,90,0));
  }
  .contact {
    position: absolute;
    left: 442px;
    top: 104px;
    color: var(--ink);
  }
  .person-name {
    font-size: 29px;
    font-weight: 700;
    line-height: 34px;
    color: var(--brand-blue);
  }
  .person-title {
    font-size: 23px;
    font-weight: 600;
    line-height: 28px;
    color: var(--brand-green);
  }
  .details {
    margin-top: 44px;
    font-size: 21px;
    line-height: 25px;
    list-style: none;
  }
  .details .label {
    font-weight: 700;
    color: var(--brand-blue);
  }
</style>
</head>
<body>
  <main class="business-card">
    <div class="brand">
      <span class="brand-name">BRV</span>
      <span class="brand-tagline">Bright Relay Ventures</span>
    </div>
    <div class="divider"></div>
    <section class="contact">
      <h1 class="person-name">Dale Orwick</h1>
      <p class="person-title">CEO</p>
      <ul class="details">
        <li>2380 Tallow St. Suite #240</li>
        <li>San Francisco, CA 94107</li>
        <li><span class="label">Phone</span> : 415-555-0138</li>
        <li><span class="label">Fax</span> : 415-555-0172</li>
        <li><span class="label">Email</span> : dorwick@brvatw.com</li>
        <li><span class="label">Web</span> : brvatw.com</li>
      </ul>
    </section>
  </main>
</body>
</html>
```